Business Card for Dental Office

I need a business card that reflects a modern day dental office, called Brindle Oak Family Dental. We specialize in general and Cosmetic Dentistry. On the front it must have the business information and the logo and the back side QR code and a place to note the appointment. I have attached the logo and a current business card for the information

Target Market(s)

Patients with Dental care need

Industry/Entity Type

Health Care

Regular size business card with round corners

Font styles to use
Other font styles liked:
• lato light font

Colors
34a7d8
0255a3
ffffff
000000
85cae6
85acd3

Requirements
Must have
• The logo, business information, website and in the a place to write down the appointment
Nice to have
• QR Code in the back

```html
<!DOCTYPE html>
<html lang="en">
<head>
<meta charset="utf-8">
<title>Brindle Oak Family Dental – Business Card</title>
<link rel="stylesheet" href="https://fonts.googleapis.com/css2?family=Source+Sans+3:ital,wght@0,400;0,600;0,700;1,700&display=swap">
<style>
  :root {
    --stage: #000000;
    --card-front: #053f5a;
    --card-front-glow: #0b4a68;
    --brand-blue: #34a7d8;
    --brand-blue-soft: #85cae6;
    --text-light: #ffffff;
    --card-back: #ffffff;
    --line-blue: #85acd3;
    --ink: #1d3a52;
    --soft-blue: #e3f3fa;
  }
  * { margin: 0; padding: 0; box-sizing: border-box; }
  html, body { width: 1200px; height: 900px; overflow: hidden; background: var(--stage); }
  body { position: relative; font-family: "Source Sans 3", sans-serif; }

  .card {
    position: absolute;
    top: 200px;
    width: 310px;
    height: 502px;
    border-radius: 0 56px 0 56px;
    overflow: hidden;
  }

  /* Front */
  .card-front { left: 265px; background: var(--card-front); color: var(--text-light); }
  .front-glow {
    position: absolute;
    left: -150px; top: -300px;
    width: 520px; height: 520px;
    border-radius: 50%;
    background: var(--card-front-glow);
  }
  .brand-mark {
    position: absolute;
    left: 124px; top: 78px;
    width: 62px; height: 62px;
    border-radius: 50%;
    background: var(--brand-blue);
  }
  .practice-name {
    position: absolute;
    left: 0; right: 0; top: 168px;
    text-align: center;
    font-size: 25px;
    font-weight: 600;
    color: var(--brand-blue);
    white-space: nowrap;
  }
  .dentist { position: absolute; left: 26px; top: 256px; }
  .dentist-name { font-size: 18px; font-weight: 600; }
  .dentist-name strong { font-weight: 700; }
  .dentist-role { font-size: 15.5px; font-weight: 600; margin-top: -1px; }
  .address { position: absolute; left: 26px; top: 341px; font-size: 13.5px; line-height: 19px; font-style: normal; }
  .contacts { position: absolute; left: 26px; top: 403px; list-style: none; font-size: 13.5px; line-height: 19.5px; }
  .contacts li { display: flex; align-items: center; gap: 6px; }
  .contacts svg { width: 10px; height: 10px; fill: var(--text-light); }

  /* Back */
  .card-back { left: 641px; background: var(--card-back); color: var(--ink); }
  .back-wash {
    position: absolute;
    right: -150px; bottom: -170px;
    width: 330px; height: 330px;
    border-radius: 50%;
    background: linear-gradient(200deg, var(--soft-blue), #ffffff 80%);
  }
  .field {
    position: absolute;
    top: 80px;
    height: 345px;
    width: 18px;
    writing-mode: vertical-rl;
    transform: rotate(180deg);
    display: flex;
    align-items: center;
    font-size: 14px;
    gap: 3px;
  }
  .field-line { flex: 1; block-size: 1px; background: var(--line-blue); }
  .field-name { left: 115px; }
  .field-date { left: 150px; }
  .field-time { left: 180px; }
  .field-time .field-line.short { flex: 0 0 125px; }
  .notice {
    position: absolute;
    left: 216px; top: 68px;
    height: 350px;
    writing-mode: vertical-rl;
    transform: rotate(180deg);
    font-size: 14px;
    font-style: italic;
    font-weight: 700;
    text-align: center;
    white-space: nowrap;
  }
</style>
</head>
<body>
  <section class="card card-front" aria-label="Card front">
    <div class="front-glow"></div>
    <div class="brand-mark" aria-hidden="true"></div>
    <h1 class="practice-name">Brindle Oak Family Dental</h1>
    <div class="dentist">
      <p class="dentist-name"><strong>Maren</strong> Holloway, D.M.D.</p>
      <p class="dentist-role">General &amp; Cosmetic Dentistry</p>
    </div>
    <address class="address">2180 Alder Crest Ave.<br>Fairview CA 90310</address>
    <ul class="contacts">
      <li><svg viewBox="0 0 10 10" aria-hidden="true"><path d="M2 0.5 L3.6 2.6 L2.7 3.6 Q4 6 6.4 7.3 L7.4 6.4 L9.5 8 L8.3 9.5 Q3.5 9 0.5 1.7 Z"/></svg>555.214.0187</li>
      <li><svg viewBox="0 0 10 10" aria-hidden="true"><rect x="1" y="1" width="8" height="8" rx="1"/></svg>555.214.0192</li>
      <li><svg viewBox="0 0 10 10" aria-hidden="true"><circle cx="5" cy="5" r="4.5"/></svg>www.brindleoakdental.com</li>
    </ul>
  </section>

  <section class="card card-back" aria-label="Card back, appointment note">
    <div class="back-wash"></div>
    <div class="field field-name"><span>Name :</span><span class="field-line"></span></div>
    <div class="field field-date"><span>Date &nbsp;:</span><span class="field-line"></span></div>
    <div class="field field-time"><span>Time &nbsp;:</span><span class="field-line short"></span><span>AM</span><span class="field-line"></span><span>PM</span></div>
    <p class="notice">If unable to keep appointment, kindly give 24hrs notice.</p>
  </section>
</body>
</html>
```